Marriage Retreat: 4 Page Color Brochure

I need a 4 page, full color brochure that is 8.5 x 11 when folded (11 x 17 front/back when printed/unfolded). The brochure is to inform pastors and religious leaders about a private retreat to help them strengthen their marriages. Attached you will find: (1) a Word document with the copy/text and initial guidelines on the page layout (although some flexibility on what text goes on which page is acceptable); (2) a creative brief PDF with some of the visual ideas I have to jumpstart your thinking; (3) logo files for the organization Steadfast Vows (the logo must be included); (4) original scan of tree artwork that can be used as a visual element (this is the same tree that has been converted to a vector file in the logo; please use a color scheme in the brochure that is complementary to this artwork). The overall feel for this piece should be timeless, classic, welcoming and approachable. The font in the logo is Audrey, although it has been stylized a bit. Please take that into account when selecting fonts for the layout. I do not yet have the photo of Dale & Norma (the hosts of this retreat) for you to include with their bios. Please insert a placeholder image for now and I will get you the actual photo in a few days. Once we get to the final stage, I would also like to have a version of the file that is laid out as 4 individual 8.5x11 pages so it can be printed in that format if needed. I would also like to have a PDF version of each file.

Target Market(s)

The initial target market for this type of service will be males (who typically recommend the service to couples), but the ultimate decision maker will probably be a female (the wife of the couple that will attend the retreat).

Industry/Entity Type

Counseling

Font styles to use
Serif
Sans Serif
Other font styles liked:
• Audrey

Colors

Designer to choose colors to be used in the design.

Requirements
Must have
• Logo for Steadfast Vows. Color scheme that is complementary to the tree artwork provided. Font that incorporates or complements the font in the logo - Audrey. Photo of Dale & Norma with their bio (use a placeholder for now). Please include at least one or two stock photos of married couples somewhere in the brochure. See the examples in the creative brief and please let me know if you need me to provide the actual files (if you do not have access to Pixmeadow Library).
Nice to have
• A design option that includes an infographic/icon style for me to consider. See creative brief document for more on this idea.
Should not have
• Note: I removed the prior instructions indicating this design should not have a full page bleed. That is no longer a limitation on this design. Feel free to go with what you think looks best to make your submission as strong as possible.

```html
<!DOCTYPE html>
<html lang="en">
<head>
<meta charset="utf-8">
<title>Steadfast Vows – Retreat Brochure Spread</title>
<link href="https://fonts.googleapis.com/css2?family=Marcellus&family=Mulish:wght@400;600;700&display=swap" rel="stylesheet">
<style>
  :root{
    --bg:#b9b9bb;
    --ink:#0f1b1c;
    --paper:#f7f7f6;
    --mist:#e4e4e5;
    --leaf:#7ab829;
    --amber:#c8861a;
    --sky:#16a9dd;
    --jade:#1fb37a;
    --text:#2f3334;
    --white:#ffffff;
  }
  *{box-sizing:border-box;margin:0;padding:0}
  html,body{width:1200px;height:840px;overflow:hidden;background:var(--bg)}
  body{font-family:"Mulish",Arial,sans-serif;color:var(--text)}
  .spread{position:absolute;left:40px;top:57px;width:1120px;height:725px;display:flex;box-shadow:0 10px 30px rgba(0,0,0,.25)}
  .page{position:relative;width:560px;height:725px;background:var(--paper);overflow:hidden}
  .page--left{border-right:1px solid #d5d5d5}
  .dark-band{position:absolute;inset:0;background:var(--ink)}
  .page--left .dark-band{clip-path:polygon(0 0,100% 0,100% 43%,0 25%)}
  .page--right .dark-band{clip-path:polygon(0 0,100% 0,100% 49%,0 42%)}
  .mist-band{position:absolute;left:0;right:0;bottom:0;background:var(--mist)}
  .page--left .mist-band{top:508px}
  .page--right .mist-band{top:492px}
  .heading{font-family:"Marcellus",Georgia,serif;text-transform:uppercase;letter-spacing:.5px;position:absolute}
  .risk-title{left:34px;top:28px;font-size:25px;color:var(--leaf)}
  .stat{position:absolute;left:34px;display:flex;align-items:center;gap:8px;color:#dfe4e4;font-size:10px;line-height:1.25}
  .stat__num{font-family:"Marcellus",Georgia,serif;font-size:26px;color:var(--amber);min-width:58px}
  .chart{position:absolute;left:0;top:0}
  .invite-title{left:34px;top:242px;font-size:22px;color:var(--amber)}
  .invite-intro{position:absolute;left:34px;top:274px;width:240px;font-size:10px;line-height:1.4}
  .retreat-box{position:absolute;left:34px;top:332px;width:246px;padding:10px 12px;border:1.5px solid var(--amber);border-radius:8px;font-size:9px;line-height:1.4}
  .retreat-box strong{font-weight:700}
  .benefits{position:absolute;left:300px;top:330px;width:230px}
  .benefit{display:flex;gap:10px;align-items:center;height:40px}
  .benefit svg{flex:none}
  .benefit__copy{flex:1;min-width:0}
  .benefit__name{font-family:"Marcellus",Georgia,serif;color:var(--amber);font-size:13px}
  .benefit__text{font-size:9px;line-height:1.3}
  .plus{height:12px;padding-left:60px;color:var(--leaf);font-weight:700;font-size:13px;line-height:12px}
  .transform-band{position:absolute;left:0;top:484px;width:470px;height:40px;background:var(--leaf);border-radius:0 20px 20px 0;color:var(--white);font-family:"Marcellus",Georgia,serif;font-size:19px;letter-spacing:.5px;text-transform:uppercase;display:flex;align-items:center;padding-left:34px}
  .quotes{position:absolute;left:24px;right:24px;display:flex;flex-direction:column;gap:8px}
  .page--left .quotes{top:536px}
  .page--right .quotes{top:504px}
  .quote{position:relative;background:var(--white);border-radius:14px;padding:7px 30px 7px 30px;font-size:8.6px;line-height:1.35;box-shadow:0 1px 2px rgba(0,0,0,.08)}
  .quote::before,.quote::after{font-family:Georgia,serif;color:var(--amber);font-size:28px;font-weight:700;position:absolute;line-height:1}
  .quote::before{content:"\201C";left:8px;top:2px}
  .quote::after{content:"\201D";right:8px;bottom:-10px}
  .host-photo{position:absolute;right:30px;top:104px;width:130px;height:80px;background:linear-gradient(135deg,#d19a2c,#b97814);border-radius:8px}
  .host-caption{position:absolute;right:30px;top:190px;width:130px;text-align:center;color:var(--white);font-size:10px;font-weight:700}
  .hosts-title{left:30px;top:186px;font-size:20px;color:var(--leaf)}
  .hosts-bio{position:absolute;left:30px;top:214px;width:500px;font-size:9.6px;line-height:1.4;color:#dfe4e4;text-align:justify}
  .brand{position:absolute;left:40px;top:370px;display:flex;align-items:center;gap:10px}
  .brand__dot{width:22px;height:22px;border-radius:50%;background:var(--leaf)}
  .brand__name{font-family:"Marcellus",Georgia,serif;font-size:24px;color:var(--ink);letter-spacing:1px}
  .promo{position:absolute;left:290px;top:346px;right:0;height:124px;background:var(--leaf);color:var(--white);padding:14px 22px}
  .promo__lead{font-family:"Marcellus",Georgia,serif;font-size:17px;line-height:1.2;margin-bottom:8px}
  .promo__body{font-family:"Marcellus",Georgia,serif;font-size:13px;line-height:1.3}
</style>
</head>
<body>
<main class="spread">
  <section class="page page--left">
    <div class="dark-band"></div>
    <h2 class="heading risk-title">Ministry Marriages Are At Risk</h2>
    <div class="stat" style="top:70px"><span class="stat__num">77%</span><span>of pastors feel they do<br>not have a good marriage</span></div>
    <div class="stat" style="top:106px"><span class="stat__num">48%</span><span>say their current ministry role<br>has been difficult on their marriage</span></div>
    <div class="stat" style="top:142px"><span class="stat__num">26%</span><span>of pastors face significant<br>marital problems</span></div>
    <svg class="chart" width="560" height="320" viewBox="0 0 560 320" aria-hidden="true">
      <g stroke="#6b7576" stroke-width=".6" fill="none">
        <line x1="200" y1="86" x2="455" y2="192"/>
        <line x1="230" y1="122" x2="445" y2="205"/>
        <line x1="190" y1="158" x2="440" y2="216"/>
      </g>
      <g fill="none" transform="rotate(-90 450 222)">
        <circle cx="450" cy="222" r="56" stroke="#16a9dd" stroke-width="12" stroke-dasharray="270.9 351.9"/>
        <circle cx="450" cy="222" r="40" stroke="#c8861a" stroke-width="12" stroke-dasharray="120.6 251.3"/>
        <circle cx="450" cy="222" r="25" stroke="#1fb37a" stroke-width="10" stroke-dasharray="40.8 157.1"/>
      </g>
    </svg>

    <h2 class="heading invite-title">Your Invitation</h2>
    <p class="invite-intro">Whether your marriage is thriving, in distress, or needs a fresh start, Steadfast Vows retreats equip couples in ministry to:</p>
    <p class="retreat-box"><strong>The 3-day retreat</strong> is personally tailored for one couple only. We provide a lovely, comfortable, private and safe setting where everything is taken care of. We can welcome you to our locations in Austin and Chicago or, in special circumstances, bring the retreat to your area.</p>

    <div class="benefits">
      <div class="benefit">
        <svg width="36" height="36" viewBox="0 0 40 40" fill="none" stroke="#7ab829" stroke-width="2"><path d="M20 33 C8 24 6 17 10 12 C13 8 18 9 20 14 C22 9 27 8 30 12 C34 17 32 24 20 33Z"/></svg>
        <div class="benefit__copy"><div class="benefit__name">Deepen Intimacy</div><div class="benefit__text">Reinvigorate love by being heard and valued</div></div>
      </div>
      <div class="plus">+</div>
      <div class="benefit">
        <svg width="36" height="36" viewBox="0 0 40 40" fill="none" stroke="#7ab829" stroke-width="2"><circle cx="14" cy="13" r="5"/><circle cx="27" cy="13" r="5"/><path d="M5 33 C5 24 23 24 23 33 M18 33 C18 24 35 24 35 33"/></svg>
        <div class="benefit__copy"><div class="benefit__name">Untangle Relational Knots</div><div class="benefit__text">Heal hurts, care for yourself and each other with grace</div></div>
      </div>
      <div class="plus">+</div>
      <div class="benefit">
        <svg width="36" height="36" viewBox="0 0 40 40" fill="none" stroke="#7ab829" stroke-width="2"><circle cx="13" cy="9" r="4"/><circle cx="27" cy="9" r="4"/><path d="M13 14 V26 M27 14 V26 M13 26 L9 36 M13 26 L17 36 M27 26 L23 36 M27 26 L31 36 M5 18 L35 18"/></svg>
        <div class="benefit__copy"><div class="benefit__name">Replenish Joy</div><div class="benefit__text">Create an environment to grow and rediscover fun</div></div>
      </div>
    </div>

    <div class="mist-band"></div>
    <div class="transform-band">Experience Transformation</div>
    <div class="quotes">
      <p class="quote">Our marriage was in crisis. The stress of ministry had taken a deep toll on us and in the worst moments we didn't even like each other anymore. Dale and Norma are people we trust with the darkest moments of our lives. They stood with us and held up our arms to allow us to continue.</p>
      <p class="quote">During a critical time, Dale and Norma helped us navigate our marriage around the traps that we so easily and repeatedly fell into… We were sitting ducks for the evil one… They took us to the deep end of the marriage pool and dove in first. I see a more fruitful and God-honoring marriage ahead.</p>
      <p class="quote">Dale and Norma understand the sanctity of safety and compassionately learning from each other's stories… the triumphs, the failures, the times of healing, and the times of deep woundedness. They hold the stories of the couples they work with tenderly, confidentially and dearly.</p>
    </div>
  </section>

  <section class="page page--right">
    <div class="dark-band"></div>
    <div class="host-photo" role="img" aria-label="Placeholder for a portrait photo of the hosts, Dale and Norma Ashby"></div>
    <p class="host-caption">Dale &amp; Norma Ashby</p>
    <h2 class="heading hosts-title">Your Hosts</h2>
    <p class="hosts-bio">Dale and Norma Ashby bring more than 20 years of experience helping build and restore Christ-centered marriages. They have experienced God's redemption in their own broken stories. A compassionate and insightful listener, Dale is a retired energy industry leader currently serving on a corporate board and church overseer board. Norma formerly served in full-time ministry and is a gifted teacher who delights in unpacking God's truth. God has used the time and tools they offer to transform many marriages.</p>

    <div class="brand"><span class="brand__dot"></span><span class="brand__name">Steadfast Vows</span></div>

    <div class="promo">
      <p class="promo__lead">A retreat for couples in ministry</p>
      <p class="promo__body">Steadfast Vows retreats provide you time, space, and Bible-based tools to cultivate a life-giving marriage.</p>
    </div>

    <div class="mist-band"></div>
    <div class="quotes">
      <p class="quote">Dale and Norma are tender-hearted, caring, full of compassion, and willing to press into the real issues to help bring needed healing and health to couples they work with… They understand the hard work it will take to get healthy and are willing to fight alongside couples to help them wrestle with the hardships they might have encountered in life and marriage… Dale and Norma are gifted with discernment and will help you navigate the wounds that are recognized and the wounds that still need to be discovered.</p>
      <p class="quote">Dale and Norma meet people in their pain and brokenness without shame or judgment and gently help them make major shifts from a place of extreme distress to a hopeful and productive path forward.</p>
      <p class="quote">This experience was the most important thing I have ever done in my life outside of saying yes to Jesus. As a pastor, I have always known that my family is my number one ministry. This experience helped me take that theoretical goal and turn it into a reality.</p>
      <p class="quote">Dale and Norma exemplify these qualities: a safety zone with in-the-vault assurance, advice grounded in scripture, a straightforward message, truth spoken in love even when painful, vulnerability and authenticity.</p>
    </div>
  </section>
</main>
</body>
</html>
```